Brochure Design Project

Using supplied logo and supplied graphics I want a 4-page brochure 81/2x 11" that can be used as a leave behind, a self mailer and a pdf email attachment for promotion purposes.
The cover needs to be visually provocative and support the following questions"
"Have you lost your leadership edge... has your company lost it's momentum... are your employees as engaged as they need to be?"
The inside of the brochure should explain the Harbor Crest Coaching 7 Step process with is explained in the attached PowerPoint.
Back page should be brief bio of me. And Statement about who we work with. I am attaching a tri-fold brochure we designed but do not like because it is bland and the graphic inside is hard to read.
Target Market(s)
"C" level executives (CEO, CIO, CFO, CMO, CRO etc)
Industry/Entity Type
Leadership
Look and feel

```html
<!DOCTYPE html>
<html lang="en">
<head>
<meta charset="utf-8">
<title>Harbor Crest Coaching – Brochure</title>
<link rel="stylesheet" href="https://fonts.googleapis.com/css2?family=Playfair+Display:wght@700&family=Lato:wght@300;400;700&family=Open+Sans:ital,wght@0,400;0,600;0,700;1,400;1,600&display=swap">
<style>
:root{
  --slate:#5d7591;
  --slate-dark:#3f5a78;
  --navy:#244b6b;
  --teal:#2c6a8c;
  --sage:#7f9479;
  --sage-dark:#4d6a5f;
  --green-text:#7e9a62;
  --mist:#e2e6ea;
  --paper:#ffffff;
  --ink:#3b4148;
  --soft-ink:#6d757e;
  --backdrop:#ece8e2;
}
*{box-sizing:border-box;margin:0;padding:0}
html,body{width:1200px;height:900px;overflow:hidden;background:var(--backdrop)}
body{font-family:"Open Sans",Arial,sans-serif;color:var(--ink)}
.canvas{position:relative;width:1200px;height:900px}
.page{position:absolute;background:var(--paper);overflow:hidden;box-shadow:0 2px 8px rgba(0,0,0,.18)}
.abs{position:absolute}

/* Cover */
.cover{left:24px;top:24px;width:325px;height:420px}
.cover-photo{left:0;top:0;width:325px;height:268px;background:linear-gradient(180deg,#dfe6ec 0%,#b9c4cf 45%,#6b7684 100%)}
.cover-strip{left:0;top:0;width:96px;height:268px;background:linear-gradient(180deg,rgba(63,90,120,.95),rgba(93,117,145,.85))}
.cover-headline{left:14px;top:20px;font-family:"Playfair Display",Georgia,serif;font-weight:700;color:#fff;font-size:23px;line-height:1.02;width:200px;text-shadow:0 1px 2px rgba(0,0,0,.25)}
.cover-brand-panel{left:0;top:268px;width:138px;height:152px;background:var(--slate)}
.cover-title-panel{left:138px;top:268px;width:187px;height:152px;background:var(--mist)}
.logo-box{left:14px;top:22px;width:110px;height:40px;background:#fff;display:flex;align-items:center;gap:4px;padding:0 6px}
.logo-dot{width:8px;height:8px;border-radius:50%;background:var(--teal);flex:none}
.logo-name{font-family:"Open Sans",Arial,sans-serif;font-weight:600;font-size:9.5px;color:var(--teal);line-height:1.1}
.cover-address{left:16px;top:76px;color:#fff;font-size:6px;line-height:1.55}
.cover-title{left:10px;top:40px;font-family:"Playfair Display",Georgia,serif;font-weight:700;color:var(--green-text);font-size:21px;line-height:1.02}

/* Back */
.back{left:24px;top:456px;width:325px;height:420px}
.back-topband{left:0;top:0;width:325px;height:72px;background:var(--navy)}
.back-tagline{left:60px;top:42px;color:#fff;font-size:9px;letter-spacing:.4px}
.back-photo{left:20px;top:76px;width:232px;height:162px;background:linear-gradient(160deg,#9a9a9a,#6a6a6a 60%,#555)}
.back-sage{left:258px;top:76px;width:67px;height:232px;background:var(--sage)}
.back-band{left:0;top:244px;width:252px;height:64px;background:var(--slate)}
.back-deep{left:258px;top:314px;width:67px;height:58px;background:var(--sage-dark)}
.back-brand{left:20px;top:326px;display:flex;align-items:center;gap:4px}
.back-brand .logo-name{font-size:7px}
.back-brand .logo-dot{width:6px;height:6px}
.back-contact{left:20px;top:338px;font-size:5.6px;line-height:1.5;color:var(--soft-ink)}
.social{left:20px;top:386px;display:flex;gap:3px}
.social span{width:8px;height:8px;background:var(--teal);display:block}
.indicia{left:256px;top:378px;width:56px;height:32px;border:1px solid #9aa2aa;font-size:4.4px;line-height:1.45;color:var(--soft-ink);text-align:center;padding-top:3px}

/* Spread */
.spread-left{left:373px;top:190px;width:401px;height:519px}
.spread-right{left:775px;top:190px;width:401px;height:519px}
.steps-bg{left:0;top:0;width:205px;height:330px;background:linear-gradient(180deg,#eef0f2,#dde1e5)}
.step-circle{left:12px;width:44px;height:44px;border-radius:50%;background:var(--navy);color:#b7c6d4;font-family:"Lato",Arial,sans-serif;font-weight:300;font-size:10px;display:flex;align-items:center;justify-content:center;letter-spacing:.3px;border:1.5px solid #eef0f2}
.step-circle.alt{background:var(--slate-dark)}
.step-circle.last{background:var(--sage);color:#e9eee6}
.step-list{left:64px;top:14px;width:136px;font-size:5.6px;line-height:1.42;color:var(--soft-ink)}
.step-list dt{color:var(--green-text);font-weight:700;font-size:6.2px;margin-top:5px}
.step-list dt:first-child{margin-top:0}
.quote-col{left:205px;top:0;width:196px;height:519px;background:linear-gradient(180deg,#5d7591,#4e6684)}
.quote-mark{font-family:"Playfair Display",Georgia,serif;color:#9fb1c4;font-size:26px;line-height:1}
.quote{left:14px;top:12px;width:172px;color:#fff;font-style:italic;font-weight:600;font-size:11.2px;line-height:1.38}
.quote-by{left:14px;top:236px;color:#dbe3ea;font-size:6px;line-height:1.5}
.bio-photo{left:14px;top:268px;width:112px;height:80px;background:linear-gradient(180deg,#8fa87a,#4f6e3e);border:3px solid #fff}
.bio{left:14px;top:362px;width:150px;color:#fff;font-size:6.4px;line-height:1.55}
.process{left:0;top:330px;width:205px;height:189px;background:#fff}
.process-title{left:14px;top:14px;font-family:"Lato",Arial,sans-serif;font-weight:400;font-size:24px;color:var(--navy)}
.process-sub{left:16px;top:44px;font-size:6.4px;font-weight:700;color:var(--sage)}
.process-intro{left:16px;top:58px;width:180px;font-style:italic;font-size:5.6px;line-height:1.5;color:var(--soft-ink)}
.process-body{left:16px;top:92px;width:180px;font-size:5.6px;line-height:1.5;color:var(--ink)}

.promise-title{left:26px;top:20px;font-family:"Lato",Arial,sans-serif;font-size:26px;color:var(--soft-ink);font-weight:300}
.promise-title b{color:var(--teal);font-weight:400}
.promise-sub{left:26px;top:58px;font-size:6.4px;font-weight:700;color:var(--teal)}
.promise-body{left:26px;top:72px;width:355px;font-size:5.8px;line-height:1.55;color:var(--soft-ink)}
.chalk-photo{left:26px;top:146px;width:252px;height:150px;background:linear-gradient(160deg,#5a5e62,#34383c);border:4px solid #fff;box-shadow:0 0 0 1px #d3d8dc}
.stat-panel{left:278px;top:146px;width:123px;height:150px;background:var(--sage);padding:14px 14px}
.stat-num{font-family:"Open Sans",Arial,sans-serif;font-size:34px;font-weight:400;color:#fff;line-height:1}
.stat-text{margin-top:8px;font-size:5.8px;line-height:1.5;color:#eef1ec;font-weight:600}
.results{left:0;top:312px;width:401px;height:207px;background:linear-gradient(180deg,#eef0f2,#e1e5e9)}
.results-title{left:26px;top:16px;width:260px;font-size:7px;font-weight:700;color:var(--teal);line-height:1.5}
.results-list{left:26px;top:46px;width:340px;list-style:none;font-size:5.8px;line-height:1.5;color:var(--soft-ink)}
.results-list li{display:flex;gap:6px;margin-bottom:4px}
.results-list li::before{content:"»";color:var(--teal);font-weight:700}
</style>
</head>
<body>
<main class="canvas">

  <!-- Front cover -->
  <section class="page cover">
    <div class="abs cover-photo" role="img" aria-label="Photograph of a group of six business executives in suits"></div>
    <div class="abs cover-strip"></div>
    <h1 class="abs cover-headline">Regain<br>Your<br>Competitive<br>Edge</h1>
    <div class="abs cover-brand-panel">
      <div class="abs logo-box"><span class="logo-dot"></span><span class="logo-name">Harbor Crest Coaching</span></div>
      <p class="abs cover-address">218 Maple Ridge Road<br>Suite 40-B<br>Easton, MD 21601<br>www.harborcrestcoach.com</p>
    </div>
    <div class="abs cover-title-panel">
      <h2 class="abs cover-title">Executive and<br>Organizational<br>Coaching</h2>
    </div>
  </section>

  <!-- Back cover / mailer -->
  <section class="page back">
    <div class="abs back-topband"><p class="abs back-tagline">Get Back on Track.</p></div>
    <div class="abs back-photo" role="img" aria-label="Photograph of a businessman on a ladder drawing a rising arrow on a wall"></div>
    <div class="abs back-sage"></div>
    <div class="abs back-band"></div>
    <div class="abs back-deep"></div>
    <div class="abs back-brand"><span class="logo-dot"></span><span class="logo-name">Harbor Crest Coaching</span></div>
    <p class="abs back-contact">218 Maple Ridge Road<br>Suite 40-B<br>Easton, MD 21601<br>T: (410) 555-0142<br>F: (410) 555-0188</p>
    <div class="abs social"><span></span><span></span><span></span></div>
    <div class="abs indicia">U.S. POSTAGE PAID<br>EASTON, MD<br>PERMIT NO. 1254<br>ZIP CODE 21601</div>
  </section>

  <!-- Inside left -->
  <section class="page spread-left">
    <div class="abs steps-bg"></div>
    <div class="abs step-circle" style="top:14px">ONE</div>
    <div class="abs step-circle alt" style="top:56px">TWO</div>
    <div class="abs step-circle" style="top:98px">THREE</div>
    <div class="abs step-circle alt" style="top:140px">FOUR</div>
    <div class="abs step-circle" style="top:182px">FIVE</div>
    <div class="abs step-circle alt" style="top:224px">SIX</div>
    <div class="abs step-circle last" style="top:266px">SEVEN</div>
    <dl class="abs step-list">
      <dt>Create a Safety Net.</dt><dd>We'll help your organization face change by exposing the benefits and challenging the fears behind it.</dd>
      <dt>Identify the Problem.</dt><dd>The next step is to evaluate the situation. We'll look at individual and team results using the LMI assessment tool.</dd>
      <dt>Dive Deep.</dt><dd>Using the Layered Insight Method, we'll map the beliefs and processes that created the crisis.</dd>
      <dt>Consensus Match.</dt><dd>Achieve a common view of the problem and create the path for alignment toward a new vision for the organization.</dd>
      <dt>SWOT Analysis.</dt><dd>We'll conduct both a SWOT and a Block Analysis to determine strengths and potential obstacles to success.</dd>
      <dt>Set Goals.</dt><dd>We'll conduct goal setting and attainment planning using the AIM SMART process.</dd>
      <dt>Meet the Mentor.</dt><dd>The meat of the process is intensive coaching on dismantling obstacles, meeting challenges and achieving the goals you articulate.</dd>
    </dl>

    <div class="abs quote-col">
      <blockquote class="abs quote"><span class="quote-mark">“</span>Whether your organization's diagnosis is mild dysfunction or complete disengagement, our job is to help you pivot. That is, find the turning point that helps you to take your pulse, regain control, breathe again and get back on the path to achieving growth.<span class="quote-mark">”</span></blockquote>
      <p class="abs quote-by">Daniel R. Whitfield, CEO<br>Harbor Crest Coaching</p>
      <div class="abs bio-photo" role="img" aria-label="Photograph of the company founder walking in a garden"></div>
      <p class="abs bio">After 30-years as a senior executive in the print and online business-to-business media business Daniel founded Harbor Crest Coaching to apply his skill and experience to help individuals and organizations facing "must change" situations. He lives in Maryland with his wife and three children.</p>
    </div>

    <div class="abs process">
      <h2 class="abs process-title">Our Process</h2>
      <p class="abs process-sub">From Distress to Success</p>
      <p class="abs process-intro">Harbor Crest Coaching provides one-on-one and group coaching focused on enabling individuals and organizations to align their values, strengths and goals to achieve extraordinary, sustainable outcomes even in the most challenging situations.</p>
      <p class="abs process-body">Harbor Crest Coaching services include up to five individual <b>LMI Assessments</b>, with one-hour, one-on-one <b>debriefings</b> conducted by LMI Master Practitioners. In addition, you'll receive five, one-hour <b>situation analysis interviews</b> with your senior management team and up to 10.5 hours of interviews with other stakeholders. We provide comprehensive Mind-Mapping, with visual representation of the results of the interviews. We present two, five-hour management group sessions to present findings and to set goals. Finally, the mentoring service includes 26 one-hour coaching sessions with each of your senior executives.</p>
    </div>
  </section>

  <!-- Inside right -->
  <section class="page spread-right">
    <h2 class="abs promise-title">Our <b>Promise</b></h2>
    <p class="abs promise-sub">Coaching Helps Inspire Individuals Toward Positive and Sustainable Action.</p>
    <p class="abs promise-body">Harbor Crest Coaching works with executives and companies that are facing issues ranging from mild dysfunction to significant distress. We help them pivot, regain control and achieve renewed growth. Harbor Crest Coaching employs the Momentum Leadership process developed by Alan M. Reyes PhD, founder of the Center for Applied Leadership Coaching (CALC). Momentum Leadership is the process that develops a personally effective style of leadership that positively influences and changes not only the leader, but also those with whom they work and interact, as well as their organization as a whole.</p>
    <div class="abs chalk-photo" role="img" aria-label="Photograph of a man in a suit facing a chalkboard full of equations"></div>
    <div class="abs stat-panel">
      <p class="stat-num">79%</p>
      <p class="stat-text">Of the thousands of companies that use some form of coaching, the vast majority use it to improve performance, according to the National Leadership Research Council 2008 Coaching Survey.</p>
    </div>
    <div class="abs results">
      <p class="abs results-title">The Harbor Crest Coaching Program is a 7-step process that results in:</p>
      <ul class="abs results-list">
        <li>Fearless, confident leaders who share understanding of the organization's situation</li>
        <li>Appreciation for what motivates each management team member, eliminating hidden agendas and second-guessing and building alignment</li>
        <li>Trust, respect and cooperation among management team members and management to focus on what brings results quickly and breaks through the "blocks" that impede progress</li>
        <li>Clearly articulated goals, measurements of success and durable confidence across the organization</li>
        <li>A win-win environment where everyone feels capable of meeting any challenge and exploiting every opportunity</li>
      </ul>
    </div>
  </section>

</main>
</body>
</html>
```